[Green Press + Juice Bar] Digital Menu Boards (2)

We need designs for our digital menu screens. Dimensions are 1080 x 1920 (9:16). Screens are in portrait mode–2 of them. They will be side by side so designs should be cohesive. We'll need the (Adobe) source files to be able to easily edit in the future.

Check out our Instagram (@pulpwell) to see current brand imagery for inspiration. Please disregard our current website design as it shows our old branding. Visit our Tastemap page to get a feel of the store flow in which the menu boards will be displayed: https://www.tastemap.example/biz/pulpwell-chicago-6

See "Larkfield Menu" attachment for content that will be incorporated into the design for 2 screens.

See "Cleanse Brochure" attachment to see current material we are using to promote our cleansing program. We would like to designate a portion of our menu to promote cleanse options, depending on how much room is available.

Also attached is a photo of our current, static menu board.

We've attached photos of color palettes we like.

Target Market(s)

Health-conscious individuals, healthy moms, fitness gurus, professionals

Industry/Entity Type

Health And Wellness

Font styles to use
Serif
Sans Serif

Colors

Designer to choose colors to be used in the design.

Requirements
Must have
• We need designs for our digital menu screens. Dimensions are 1080 x 1920 (9:16). Screens are in portrait mode–2 of them. We'll need the (Adobe) source files to be able to easily edit in the future. To ensure the sizing of the outputted file is correct and spaced correctly, send us a test file to test on our TV.
Nice to have
• Ideally, the menu will reflect current branding with font usage of one or more of the following:
• FuturaStd-Bold
• Desiderata-Regular
• Wisdom Script
• Bernier Typeface
• Swistblnk Banthers
• Hanley
• If there is space, we'd like to have space to roll a photo/video slideshow on the menu.

```html
<!DOCTYPE html>
<html lang="en">
<head>
<meta charset="utf-8">
<title>Green Press + Juice Bar — Larkfield Menu</title>
<link rel="stylesheet" href="https://fonts.googleapis.com/css2?family=Cinzel+Decorative:wght@700&family=Fira+Sans:wght@400;600&family=Lobster&display=swap">
<style>
  :root {
    --board: #000000;
    --ink: #ffffff;
    --bowls: #eda06d;
    --bites: #b4c27a;
    --soups: #dfb33c;
    --rule: #8a8a8a;
  }
  * { margin: 0; padding: 0; box-sizing: border-box; }
  html, body { width: 675px; height: 1200px; overflow: hidden; background: var(--board); }
  .menu-board {
    position: relative; width: 675px; height: 1200px; overflow: hidden;
    background: var(--board); color: var(--ink);
    font-family: "Fira Sans", sans-serif; text-align: center;
  }
  .block { position: absolute; left: 0; width: 675px; }
  .section-head {
    font-family: "Lobster", cursive; font-size: 46px; line-height: 52px; height: 52px;
    display: flex; align-items: center; justify-content: center; gap: 10px;
  }
  .section-head .size { font-family: "Fira Sans", sans-serif; font-weight: 600; font-size: 19px; }
  .flourish { width: 78px; height: 6px; border-radius: 3px; }
  .bowls { color: var(--bowls); }
  .bites { color: var(--bites); }
  .soups { color: var(--soups); }
  .item-name {
    font-family: "Cinzel Decorative", serif; font-weight: 700;
    font-size: 22px; line-height: 24px; letter-spacing: 0.5px; white-space: nowrap;
  }
  .item-name.two-line { line-height: 28px; }
  .price { font-family: "Fira Sans", sans-serif; font-weight: 600; font-size: 17px; margin-left: 6px; }
  .note { font-family: "Fira Sans", sans-serif; font-weight: 600; font-size: 13px; margin-left: 6px; }
  .desc { font-size: 14px; line-height: 18.5px; margin-top: 5px; white-space: nowrap; }
  .desc.loose { line-height: 21px; }
  .desc.airy { margin-top: 8px; }
  .label { color: var(--bowls); }
  .rule {
    position: absolute; left: 214px; width: 246px; height: 0;
    border-top: 1px dotted var(--rule);
  }
</style>
</head>
<body>
<main class="menu-board">

  <header class="block section-head bowls" style="top:18px">Bowls <span class="size">20oz</span></header>

  <section class="block" style="top:80px">
    <h2 class="item-name">Matcha Bowl<span class="price bowls">12.5</span></h2>
    <p class="desc"><span class="label">BASE:</span> Fresh-cracked Coconut Water, Coconut Meat, Banana, Spinach,<br>Medjool Dates, Tocotrienols, Maca, Matcha, Spirulina <span class="label">+ TOPPINGS:</span> Hemp Seeds, Blueberries,<br>Cacao Nibs, Coconut Shreds, Kiwi, Pomegranate Seeds, Banana, Bee Pollen, Mint Sprig</p>
  </section>
  <div class="rule" style="top:172px"></div>

  <section class="block" style="top:188px">
    <h2 class="item-name">Orchard Mystic<span class="price bowls">12</span></h2>
    <p class="desc"><span class="label">BASE:</span> Acai, Fresh-pressed Apple Juice, Cherries, Banana, Strawberry, Pomegranate<br><span class="label">+ TOPPINGS:</span> Seasonal Berries, Banana, Sprouted Almond Butter, Coconut Shreds, Goji Berries,<br>Bee Pollen, Housemade Coconut Whip, Housemade Raw Granola, Local Honey</p>
  </section>
  <div class="rule" style="top:282px"></div>

  <section class="block" style="top:294px">
    <h2 class="item-name">Motley Marmoset<span class="price bowls">12</span></h2>
    <p class="desc"><span class="label">BASE:</span> Acai, Housemade Almond Milk, Bananas, Blueberries, Peanut Butter, Medjool Dates<br><span class="label">+ TOPPINGS:</span> Housemade Raw Granola, Raw Chocolate Hearts, Peanut Butter, Raw Cacao<br>Drizzle, Banana, Dried Banana Chips, Cacao Nibs, Local Honey, Bee Pollen</p>
  </section>
  <div class="rule" style="top:395px"></div>

  <section class="block" style="top:412px">
    <h2 class="item-name">Keto Bowl<span class="price bowls">13</span><span class="note bowls">*under 15 net carbs*</span></h2>
    <p class="desc loose"><span class="label">BASE:</span> Acai, Housemade Almond Milk, Coconut Meat, Avocado, Blueberries, Cauliflower,<br>Pineapple, Sprouted Almond Butter, Xylitol <span class="label">+ TOPPINGS:</span> Seasonal Berries, Coconut Shreds,<br>Bee Pollen, Hemp Seeds, Mulberries, Chia Seeds</p>
  </section>
  <div class="rule" style="top:510px"></div>

  <section class="block" style="top:522px">
    <h2 class="item-name">Build Your Own Bowl<span class="price bowls">12.5</span></h2>
    <p class="desc"><span class="label">STEP 1:</span> Start with Your Liquid: Almond Milk, Apple Juice, Coconut Water<br><span class="label">+ STEP 2:</span> Choose up to 2 fruits/veggies (all bowls include banana) <span class="label">+ STEP 3:</span> Choose up to<br>2 Superfood Add-ins <span class="label">+ STEP 4:</span> Choose up to 4 Superfood Toppings<br><span class="label">+ STEP 5:</span> Choose a Sweetener (Medjool Dates, Local Honey, Xylitol)</p>
  </section>

  <header class="block section-head bites" style="top:650px">
    <span class="flourish" role="img" aria-label="Decorative swash flourish" style="background:var(--bites)"></span>
    Bites
    <span class="flourish" role="img" aria-label="Decorative swash flourish" style="background:var(--bites)"></span>
  </header>

  <section class="block" style="top:712px">
    <h2 class="item-name two-line">Hot Oatmeal + Seasonal Fruit + Superfood<br>Toppings<span class="price bites">7.5</span><span class="note bites">*served until 10:30am*</span></h2>
  </section>
  <div class="rule" style="top:776px"></div>

  <section class="block" style="top:790px">
    <h2 class="item-name">Avocado Toast<span class="price bites">2 slices: 8.5 | 1 slice : 4.5</span></h2>
    <p class="desc airy">Sprouted Harvest Seven-Grain Bread, Avocado, Pomegranate, Fig, Rosemary</p>
  </section>
  <div class="rule" style="top:848px"></div>

  <section class="block" style="top:866px">
    <h2 class="item-name">Orange Cacao Toast<span class="price bites">2 slices: 8.5 | 1 slice : 4.5</span><span class="note bites">*seasonal*</span></h2>
    <p class="desc">Sprouted Harvest Cinnamon Raisin Bread, Sprouted Almond Butter, Orange,<br>Cacao Nibs, Local Honey, Basil</p>
  </section>

  <header class="block section-head soups" style="top:958px">
    <span class="flourish" role="img" aria-label="Decorative swash flourish" style="background:var(--soups)"></span>
    Soups
    <span class="flourish" role="img" aria-label="Decorative swash flourish" style="background:var(--soups)"></span>
  </header>

  <section class="block" style="top:1022px">
    <h2 class="item-name">Broccoli “Cheddar” Soup<span class="price soups">16oz</span><span class="note soups">*Dairy Free*</span></h2>
    <p class="desc loose">Red Pepper, Carrot, Cashew, Spring Onion, Lemon, Maple, Nutritional Yeast,<br>Pink Salt, Chili Powder, Garlic Powder, Broccoli</p>
  </section>

  <section class="block" style="top:1116px">
    <h2 class="item-name">Veggie Soup with Sprouted Lentil<span class="price soups">16oz</span></h2>
    <p class="desc">Leek, Kale, Celery, Red Pepper, Green Onion, Liquid Aminos, Fresh Ginger,<br>Fresh Garlic, Lemon, Salt, Pepper, Cumin, Turmeric, Sprouted Lentils</p>
  </section>

</main>
</body>
</html>
```